Learning platform for primary and secondary schools needs a new design

We need to restyle the website: www.pennaboschetto.org.
We are developing new functionalities that will enable to turn the platform in an interactive e-learning center for teachers, parents and pupils. Our target is providing contents and learning methods for primary and secondary school.
We want to give a new structure to the homepage and all menu sections and to find a new design that facilitates users to orientate themselves. We love our main picture and we would like to emphasize it. We like our logo and we don't want to change it.
The homepage should fulfil three main tasks:
- welcome visitors;
- encourage visitors to explore three areas of free contents: learning (scopri), experimenting (esperimenti), cooking (ricette)
- convert visitors in logged users (users can register as teachers, parents or students).
We also need a new design for:
- log-in page,
- slideshow,
- galleries of pictures,
- blog page,
- newsletter.
If you have any questions, do not hesitate to contact me.
Good job!
Giulia
Updates
Hi guys,
First of all I'd like to say thanks to all designers that submitted their ideas.
Up to now I didn't find any design that really convinced me, that's why I decided to share with you a design idea that could make easier your job (please see again the project briefing). I can't wait to see your new designs!
Good job
Ciao
Giuliabetta
Hi guys,
I would like to thank you for all your wonderful design proposals. We have just launched a friends and family voting pool to help us in getting the final decision. We'll let you know the result as soon as possible within tomorrow.
Ciao
Giuliabetta
Target Market(s)
Italian teachers, parents and students attending primary and secondary school
Industry/Entity Type
Cooking
Look and feel
Each slider illustrates characteristics of the customer's brand and the style your logo design should communicate.

```html
<!DOCTYPE html>
<html lang="it">
<head>
<meta charset="utf-8">
<title>PennaBoschetto – Benvenuti</title>
<link href="https://fonts.googleapis.com/css2?family=Open+Sans:wght@400;600;700;800&display=swap" rel="stylesheet">
<style>
:root{
  --green-dark:#1f4a12;
  --green:#3f7a1c;
  --green-mid:#5b9a2a;
  --green-light:#7fb23e;
  --orange:#f07d12;
  --brown:#4a1e0c;
  --brown-soft:#5e2a12;
  --grey-bg:#ececec;
  --card:#ffffff;
  --text:#555555;
  --blue:#1f5fae;
  --pink:#d4257e;
  --mint:#bfe8da;
}
*{box-sizing:border-box;margin:0;padding:0}
html,body{width:1200px;height:2304px;overflow:hidden}
body{font-family:"Open Sans",Arial,sans-serif;color:var(--text);background:#fff;font-size:15px}
.topbar{height:32px;background:var(--green-dark);color:#d9e8cc;font-size:12px;display:flex;justify-content:space-between;align-items:center;padding:0 150px}
.topbar .right{display:flex;gap:16px;align-items:center}
.topbar .social{display:flex;gap:6px}
.topbar .social span{width:14px;height:14px;background:#8fb56a;border-radius:3px}
.header{height:168px;background:linear-gradient(#4f8a23,#2f6512);position:relative;padding:0 150px}
.brand{position:absolute;left:150px;top:40px;display:flex;align-items:center;gap:12px;color:#fff;font-weight:800;font-size:26px}
.brand .dot{width:44px;height:44px;border-radius:50%;background:var(--orange)}
.search{position:absolute;right:150px;top:22px;width:220px;height:30px;background:#fff;border-radius:3px;font-size:12px;color:#999;padding:6px 10px}
.nav{position:absolute;right:150px;top:104px;display:flex;gap:6px}
.nav a{color:#fff;text-decoration:none;font-size:16px;padding:8px 16px;font-weight:600}
.nav a.active{background:var(--orange);border-radius:3px}
.hero{height:600px;background:linear-gradient(var(--mint) 0%,#d8f0e6 55%,#8fc24d 78%,#4f7d22 100%)}
.welcome{height:210px;background:linear-gradient(var(--brown-soft),var(--brown));text-align:center;color:#fff;padding-top:38px}
.welcome h1{font-size:46px;font-weight:800;letter-spacing:2px;margin-bottom:18px}
.welcome p{width:880px;margin:0 auto;font-size:19px;font-weight:700;line-height:1.35;text-align:left}
.areas{height:380px;background:var(--grey-bg);display:flex;justify-content:center;gap:50px;padding-top:40px}
.area{width:260px;height:270px;background:var(--card);border-radius:6px;box-shadow:0 2px 6px rgba(0,0,0,.15);text-align:center;padding:26px 26px}
.area .icon{width:56px;height:44px;margin:0 auto 12px;border-radius:6px}
.area h2{font-size:22px;color:var(--green);font-weight:700;margin-bottom:10px}
.area p{font-size:13px;line-height:1.5;text-align:left}
.area a{display:block;text-align:right;color:var(--green);font-size:13px;margin-top:10px;text-decoration:none}
.roles{height:360px;background:linear-gradient(#6aa43a,#3f7a1c);display:flex;justify-content:center;gap:0;padding-top:50px}
.role{width:300px;height:260px;background:#fff;border-top:8px solid var(--blue);padding:16px 18px;position:relative}
.role.orange{border-color:var(--orange)}
.role.pink{border-color:var(--pink)}
.role h3{font-size:21px;font-weight:700;color:var(--blue);margin-bottom:10px;border-bottom:1px solid #ddd;padding-bottom:8px}
.role.orange h3{color:var(--orange)}
.role.pink h3{color:var(--pink)}
.role ul{list-style:none;font-size:13px;line-height:1.6}
.role li::before{content:"• ";color:var(--green)}
.role .btn{position:absolute;left:18px;bottom:36px;background:var(--blue);color:#fff;font-size:13px;padding:6px 14px;border-radius:3px}
.role.orange .btn{background:var(--orange)}
.role.pink .btn{background:var(--pink)}
.role .pic{position:absolute;right:18px;bottom:18px;width:90px;height:80px;border-radius:40%;background:linear-gradient(#c88a4a,#6b3b1a)}
.role.pink .pic{background:linear-gradient(#f6c8d8,#b77c43)}
.partners{height:175px;background:#fff;display:flex;justify-content:center;align-items:center;gap:46px}
.partners span{width:100px;height:80px;background:#d9dfd3;border-radius:8px}
.partners span:nth-child(odd){border-radius:50%;width:80px}
.footer{height:345px;background:linear-gradient(#5c8f32,#3f6d1c);display:flex;justify-content:center;gap:50px;padding-top:36px;color:#e7f1dc}
.footer .col{width:230px}
.footer h4{font-size:22px;font-weight:600;color:#fff;border-bottom:1px solid rgba(255,255,255,.4);padding-bottom:6px;margin-bottom:12px}
.footer p,.footer li{font-size:13px;line-height:1.6;list-style:none}
.footer .field{height:28px;background:#fff;border-radius:3px;margin-top:12px;color:#999;font-size:12px;padding:5px 8px;display:flex;justify-content:space-between}
.footer .field b{background:var(--orange);color:#fff;padding:0 8px;border-radius:2px;font-weight:600}
.bottombar{height:34px;background:var(--green-dark);color:#cfe0bd;font-size:12px;display:flex;justify-content:space-between;align-items:center;padding:0 150px}
</style>
</head>
<body>
<div class="topbar"><span>Call Us: +39 000 4821</span><div class="right"><span>Help | Sign up</span><div class="social"><span></span><span></span><span></span></div></div></div>
<header class="header">
  <div class="brand"><span class="dot"></span>PennaBoschetto</div>
  <div class="search">Search</div>
  <nav class="nav"><a class="active">Home</a><a>Scopri</a><a>Esperimenti</a><a>Ricette</a><a>Blog</a><a>Glossario</a><a>Il Progetto</a></nav>
</header>
<div class="hero" role="img" aria-label="Illustrazione: scuola colorata con bambini che giocano sul prato e arcobaleno"></div>
<section class="welcome">
  <h1>BENVENUTI</h1>
  <p>PENNABOSCHETTO.IT È UN PROGETTO SPERIMENTALE DI DIDATTICA DELLA SCIENZA IN CUI IL CIBO È PROPOSTO COME STRUMENTO PER STIMOLARE IL PENSIERO SCIENTIFICO E LA CONSAPEVOLEZZA DI QUANTO SIA IMPORTANTE UN'ALIMENTAZIONE SANA.</p>
</section>
<section class="areas">
  <div class="area"><div class="icon" style="background:#3b82c8"></div><h2>SCOPRI</h2><p>Lorem ipsum dolor sit amet consectetur adipiscing elit sed do eiusmod tempor incididunt ut labore et dolore magna aliqua ut enim ad minim veniam.</p><a>Read more ›</a></div>
  <div class="area"><div class="icon" style="background:#e8641a"></div><h2>ESPERIMENTI</h2><p>Lorem ipsum dolor sit amet consectetur adipiscing elit sed do eiusmod tempor incididunt ut labore et dolore magna aliqua ut enim ad minim veniam.</p><a>Read more ›</a></div>
  <div class="area"><div class="icon" style="background:#a3202a"></div><h2>RICETTE</h2><p>Lorem ipsum dolor sit amet consectetur adipiscing elit sed do eiusmod tempor incididunt ut labore et dolore magna aliqua ut enim ad minim veniam.</p><a>Read more ›</a></div>
</section>
<section class="roles">
  <div class="role"><h3>SONO UN INSEGNANTE</h3><ul><li>Lorem ipsum dolor sit amet</li><li>Consectetur adipiscing elit</li></ul><span class="btn">Read More</span><div class="pic" role="img" aria-label="Cioccolatini"></div></div>
  <div class="role orange"><h3>SONO UN INSEGNANTE</h3><ul><li>Lorem ipsum dolor sit amet</li><li>Consectetur adipiscing elit</li></ul><span class="btn">Read More</span><div class="pic" role="img" aria-label="Torta al cioccolato"></div></div>
  <div class="role pink"><h3>SONO UN INSEGNANTE</h3><ul><li>Lorem ipsum dolor sit amet</li><li>Consectetur adipiscing elit</li></ul><span class="btn">Read More</span><div class="pic" role="img" aria-label="Cupcake glassato"></div></div>
</section>
<section class="partners"><span></span><span></span><span></span><span></span><span></span><span></span><span></span></section>
<footer class="footer">
  <div class="col"><h4>About us</h4><p>Lorem ipsum dolor sit amet consectetur adipiscing elit sed do eiusmod tempor incididunt ut labore et dolore magna aliqua ut enim.</p></div>
  <div class="col"><h4>Site map</h4><ul><li>Home</li><li>Scopri</li><li>Esperimenti</li><li>Ricette</li><li>Blog</li><li>Glossario</li><li>Il Progetto</li></ul></div>
  <div class="col"><h4>Latest Tweet</h4><p>Nuove ricette per la scuola primaria in arrivo questa settimana.</p><p>2 hours ago</p></div>
  <div class="col"><h4>Newsletter</h4><p>Iscriviti per ricevere le novità su ricette, esperimenti e percorsi didattici.</p><div class="field">Email address<b>Go</b></div></div>
</footer>
<div class="bottombar"><span>Copyright © 2014 PennaBoschetto. All Rights Reserved.</span><span>Help | Privacy</span></div>
</body>
</html>
```